Business Card Design Project

Our organization is in need of a business card design with the use of our logo. We are looking for professional design that will embellish the image our consulting firm.

Here is a summary of what we do: Quorvent is systems consulting firm that specializes in the management, migration, and maintenance of IT infrastructure solutions.

Here is a link to my website: http://quorvent-example.com

I have attached the logo.

Target Market(s)

Organization that need IT and server support.

Industry/Entity Type

Business

```html
<!DOCTYPE html>
<html lang="en">
<head>
<meta charset="utf-8">
<title>Quorvent Business Cards</title>
<link href="https://fonts.googleapis.com/css2?family=Questrial&display=swap" rel="stylesheet">
<style>
  :root {
    --navy: #1f2a5c;
    --orange: #f07124;
    --paper: #ffffff;
    --canvas: #ffffff;
    --shadow: rgba(0, 0, 0, 0.45);
  }
  * { box-sizing: border-box; margin: 0; padding: 0; }
  html, body {
    width: 1172px; height: 1200px; overflow: hidden;
    background: var(--canvas);
    font-family: "Questrial", "Century Gothic", sans-serif;
  }
  .sheet {
    position: relative; width: 1172px; height: 1200px;
    display: grid;
    grid-template-columns: 300px 300px;
    grid-template-rows: 446px 446px;
    column-gap: 70px; row-gap: 90px;
    justify-content: center; align-content: center;
  }
  .card {
    position: relative; width: 300px; height: 446px;
    box-shadow: 8px 8px 10px var(--shadow);
  }
  .card--front { background: var(--paper); border: 1px solid #e4e4e4; }
  .card--back-orange { background: var(--orange); }
  .card--back-navy { background: var(--navy); }

  .brand {
    position: absolute; left: 34px; top: 38px;
    display: flex; align-items: center; gap: 14px;
  }
  .brand__dot { width: 26px; height: 26px; border-radius: 50%; }
  .brand__name { font-size: 27px; color: var(--navy); letter-spacing: 0.2px; }
  .theme-navy .brand__dot { background: var(--navy); }
  .theme-orange .brand__dot { background: var(--orange); }

  .person {
    position: absolute; left: 0; right: 0; top: 156px; text-align: center; color: var(--navy);
  }
  .person__name { font-size: 20px; }
  .person__title { font-size: 11px; margin-top: 6px; }

  .company {
    position: absolute; left: 0; right: 0; top: 272px; text-align: center;
    color: var(--navy); font-size: 12px; line-height: 22px;
  }

  .contacts {
    position: absolute; left: 66px; top: 344px; list-style: none;
    color: var(--navy); font-size: 14px;
  }
  .contacts li { display: flex; align-items: center; gap: 6px; height: 22px; }
  .contacts svg { width: 15px; height: 15px; flex: none; }
  .theme-navy .contacts .icon-bg { fill: var(--orange); }
  .theme-navy .contacts .icon-line { stroke: #fff; }
  .theme-orange .contacts .icon-bg { fill: none; stroke: var(--navy); stroke-width: 1.4; }
  .theme-orange .contacts .icon-line { stroke: var(--navy); }

  .back-mark {
    position: absolute; inset: 0;
    display: flex; flex-direction: column; align-items: center; justify-content: center; gap: 22px;
  }
  .back-mark__dot { width: 70px; height: 70px; border-radius: 50%; }
  .back-mark__name { font-size: 30px; }
  .card--back-orange .back-mark__dot { background: var(--paper); }
  .card--back-orange .back-mark__name { color: var(--paper); }
  .card--back-navy .back-mark__dot { background: var(--orange); }
  .card--back-navy .back-mark__name { color: var(--orange); }
</style>
</head>
<body>
<main class="sheet">

  <section class="card card--front theme-navy">
    <div class="brand"><span class="brand__dot"></span><span class="brand__name">Quorvent</span></div>
    <div class="person">
      <p class="person__name">Marcus Ellison Jr</p>
      <p class="person__title">Principal &amp; Chief Systems Engineer</p>
    </div>
    <div class="company">
      <p>Quorvent, Inc.</p>
      <p>4410 Loop Road W Fairbend, Tx 78000</p>
    </div>
    <ul class="contacts">
      <li><svg viewBox="0 0 16 16"><circle class="icon-bg" cx="8" cy="8" r="7.5"/><g class="icon-line" fill="none" stroke-width="1"><circle cx="8" cy="8" r="4.5"/><ellipse cx="8" cy="8" rx="2" ry="4.5"/><line x1="3.5" y1="8" x2="12.5" y2="8"/></g></svg>http://quorvent-example.com</li>
      <li><svg viewBox="0 0 16 16"><circle class="icon-bg" cx="8" cy="8" r="7.5"/><g class="icon-line" fill="none" stroke-width="1"><rect x="4" y="5" width="8" height="6"/><polyline points="4,5 8,8.5 12,5"/></g></svg>mell@quorvent-example.com</li>
      <li><svg viewBox="0 0 16 16"><circle class="icon-bg" cx="8" cy="8" r="7.5"/><path class="icon-line" fill="none" stroke-width="1.4" d="M5 4.5 L6.5 4.5 L7 6.5 L6 7.3 Q7 9.3 8.8 10 L9.6 9 L11.5 9.5 L11.5 11 Q8 11.5 5.5 8.5 Q4.5 6.5 5 4.5Z"/></svg>555.014.2290</li>
      <li><svg viewBox="0 0 16 16"><circle class="icon-bg" cx="8" cy="8" r="7.5"/><g class="icon-line" fill="none" stroke-width="1"><rect x="4.5" y="7" width="7" height="4.5"/><rect x="6" y="4" width="4" height="3"/></g></svg>555.014.7781</li>
    </ul>
  </section>

  <section class="card card--back-orange">
    <div class="back-mark"><span class="back-mark__dot"></span><span class="back-mark__name">Quorvent</span></div>
  </section>

  <section class="card card--front theme-orange">
    <div class="brand"><span class="brand__dot"></span><span class="brand__name">Quorvent</span></div>
    <div class="person">
      <p class="person__name">Marcus Ellison Jr</p>
      <p class="person__title">Principal &amp; Chief Systems Engineer</p>
    </div>
    <div class="company">
      <p>Quorvent, Inc.</p>
      <p>4410 Loop Road W Fairbend, Tx 78000</p>
    </div>
    <ul class="contacts">
      <li><svg viewBox="0 0 16 16"><circle class="icon-bg" cx="8" cy="8" r="7"/><g class="icon-line" fill="none" stroke-width="1"><circle cx="8" cy="8" r="4.5"/><ellipse cx="8" cy="8" rx="2" ry="4.5"/><line x1="3.5" y1="8" x2="12.5" y2="8"/></g></svg>http://quorvent-example.com</li>
      <li><svg viewBox="0 0 16 16"><circle class="icon-bg" cx="8" cy="8" r="7"/><g class="icon-line" fill="none" stroke-width="1"><rect x="4" y="5" width="8" height="6"/><polyline points="4,5 8,8.5 12,5"/></g></svg>mell@quorvent-example.com</li>
      <li><svg viewBox="0 0 16 16"><circle class="icon-bg" cx="8" cy="8" r="7"/><path class="icon-line" fill="none" stroke-width="1.2" d="M5 4.5 L6.5 4.5 L7 6.5 L6 7.3 Q7 9.3 8.8 10 L9.6 9 L11.5 9.5 L11.5 11 Q8 11.5 5.5 8.5 Q4.5 6.5 5 4.5Z"/></svg>555.014.2290</li>
      <li><svg viewBox="0 0 16 16"><circle class="icon-bg" cx="8" cy="8" r="7"/><g class="icon-line" fill="none" stroke-width="1"><rect x="4.5" y="7" width="7" height="4.5"/><rect x="6" y="4" width="4" height="3"/></g></svg>555.014.7781</li>
    </ul>
  </section>

  <section class="card card--back-navy">
    <div class="back-mark"><span class="back-mark__dot"></span><span class="back-mark__name">Quorvent</span></div>
  </section>

</main>
</body>
</html>
```